BRW Trifold Brochure

Would like a Trifold Brochure to use for marketing purposes. The company, Bright Ridge Works is a Handyman Service that offers Residential Home Repairs, Commercial Repairs, Drain Cleaning, Carpet Cleaning and Water Extraction.

I am attaching some pdf files to use as potential verbage and a copy of our business card and logo image file.

Would like to portray a professional image that sets us apart from a "mom and pops" type handyman service.

Industry/Entity Type

Marketing

```html
<!DOCTYPE html>
<html lang="en">
<head>
<meta charset="utf-8">
<title>BRW Trifold Brochure</title>
<link rel="stylesheet" href="https://fonts.googleapis.com/css2?family=Open+Sans:ital,wght@0,400;0,600;0,700;0,800;1,700&family=Oswald:wght@500;600&display=swap">
<style>
:root{
  --navy:#1d2536;
  --ink:#222831;
  --paper:#ffffff;
  --panel-grey:#e2e2e2;
  --backdrop:#ece9e2;
  --white:#ffffff;
}
*{box-sizing:border-box;margin:0;padding:0}
html,body{width:1200px;height:543px;overflow:hidden}
body{background:var(--backdrop);font-family:"Open Sans",Arial,sans-serif;color:var(--ink);position:relative}
.panel{position:absolute;top:65px;height:408px;padding:14px 10px}
.sheet-shadow{position:absolute;top:65px;height:408px;box-shadow:0 2px 8px rgba(0,0,0,.25)}
.light{background:var(--paper)}
.dark{background:var(--navy);color:var(--white)}
.body-text{font-size:5.6px;line-height:1.55;text-align:justify}
.center{text-align:center}
h2.small-head{font-size:6.6px;font-weight:700;margin-bottom:5px}
.photo{position:absolute;border-radius:1px}
.abs{position:absolute}
.brand-name{position:absolute;left:207px;width:181px;top:118px;text-align:center;font-family:"Open Sans",Arial,sans-serif;font-weight:700;font-size:15px;color:var(--white);line-height:1.2}
.brand-name .mark{display:inline-block;width:8px;height:8px;background:var(--white);margin-right:5px;vertical-align:1px}
.cover-title{position:absolute;left:207px;width:181px;top:222px;text-align:center;font-family:"Oswald",sans-serif;font-weight:600;color:var(--white);line-height:.98}
.cover-title .line{display:block;font-size:19px}
.cover-title .line.big{font-size:28px}
.cover-tag{position:absolute;left:207px;width:181px;top:297px;text-align:center;font-size:5.8px;font-weight:600;color:var(--white)}
.cover-call{position:absolute;left:207px;width:181px;top:368px;text-align:center;font-family:"Oswald",sans-serif;font-weight:500;color:var(--white);font-size:13px;line-height:1.35}
.service-list{position:absolute;left:975px;top:78px;width:150px;font-size:5.4px;line-height:1.45}
.service-group{display:grid;grid-template-columns:72px 1fr;margin-bottom:13px}
.service-group dt{font-weight:700}
.call-band{position:absolute;left:953px;top:456px;width:182px;height:17px;background:var(--navy);color:var(--white);font-style:italic;font-weight:700;font-size:8px;text-align:center;line-height:17px}
</style>
</head>
<body>

<!-- outside sheet -->
<div class="sheet-shadow" style="left:27px;width:543px"></div>

<section class="panel light" style="left:27px;width:180px">
  <h2 class="small-head center" style="margin-top:4px">RIVERTON MAINTENANCE.</h2>
  <p class="center" style="font-size:5.6px;line-height:1.6">The services you need.<br>The quality you expect.<br>Prices you can afford!!!</p>
  <p class="body-text" style="margin-top:22px">Bright Ridge Works is the professional answer to your all of your home maintenance needs. Our courteous and knowledgable staff have the skills necessary to resolve your issues at a price that you can afford. Bright Ridge Works offers Handyman Services, Carpet Cleaning, Tile &amp; Grout Cleaning and Drain Cleaning Services. If you are looking for an affordable solutions to your home upkeep needs then give Bright Ridge Works a Call Today and see what we can do for you!!!</p>
  <h2 class="small-head" style="margin-top:22px;font-size:6px">Handyman Service</h2>
</section>
<div class="photo" role="img" aria-label="House photo with green labels for roofing, siding, gutters, windows, doors, exterior repairs and interior trim" style="left:47px;top:265px;width:133px;height:90px;background:linear-gradient(160deg,#a9c4de 0%,#c9b79a 45%,#6f8a4e 100%)"></div>
<p class="body-text abs" style="left:37px;top:360px;width:160px">We're here for you! Have a leaky faucet or a toilet that runs? Would you like to hang blinds or repair a hole in the wall? How about a fresh coat of paint in the bathroom? If you don't know how, don't have the time or just don't want to do it yourself give Bright Ridge Works a call and let us show you what we can do...</p>

<section class="panel dark" style="left:207px;width:181px"></section>
<div class="brand-name"><span class="mark"></span>Bright Ridge Works</div>
<div class="cover-title"><span class="line">BRIGHT</span><span class="line">RIDGE</span><span class="line big">WORKS</span></div>
<div class="cover-tag">Service you can count on!!!</div>
<div class="cover-call">CALL TODAY !!!<br>(785) 555-0142</div>

<section class="panel light" style="left:388px;width:182px;padding-top:14px">
  <h2 class="small-head" style="font-size:6px">Drain Cleaning Services</h2>
  <p class="body-text">Bright Ridge Works can handle all of your drain cleaning needs. Floor Drains, Tub Drains, Toilet, Sinks and Main Sewer Lines, we've got you covered. Bright Ridge Works's knowledgable technicians have the skills and resources necessary to get you running again. Give us a Call Today to find out about our services and affordable prices.</p>
</section>
<div class="abs" style="left:388px;top:152px;width:182px;height:60px;background:var(--panel-grey)"></div>
<div class="photo" role="img" aria-label="Technician cleaning a drain" style="left:401px;top:155px;width:72px;height:55px;background:linear-gradient(135deg,#b8875a,#5b4636)"></div>
<div class="photo" role="img" aria-label="Carpet being cleaned" style="left:476px;top:155px;width:84px;height:55px;background:linear-gradient(135deg,#d9d6cf,#8e8a82)"></div>
<h2 class="small-head abs" style="left:398px;top:219px;font-size:6px">Carpet Cleaning &amp; Water Extraction</h2>
<p class="body-text abs" style="left:398px;top:230px;width:162px">Bright Ridge Works has your carpet cleaning needs covered. The right equipment and the right experience. Whether it is a routine cleaning or deep stain and odor removal we'll make sure you're taken care of. In need of Emergency Water Extraction? We do that too! Give us a Call Today to see what we can do for you..</p>
<h2 class="small-head abs" style="left:398px;top:304px;font-size:6px">Tile &amp; Grout Cleaning Services</h2>
<div class="abs" style="left:388px;top:318px;width:182px;height:62px;background:var(--panel-grey)"></div>
<div class="photo" role="img" aria-label="Clean tiled floor" style="left:443px;top:321px;width:70px;height:55px;background:linear-gradient(135deg,#e8e2d4,#9a8e78)"></div>
<p class="body-text abs" style="left:398px;top:385px;width:162px">You mop and you scrub but is that enough? With our tile and grout cleaning equipment you will truly be amazed with the results. Kitchen and bathroom tile, floor or wall and don't forget the grout. Give us a try, you won't regret it. Call Today and schedule your appointment.</p>

<!-- inside sheet -->
<div class="sheet-shadow" style="left:593px;width:542px"></div>

<section class="panel light" style="left:593px;width:180px">
  <h2 class="small-head center" style="margin:0;line-height:1.4">RIVERMOOR<br>CARPET SERVICE</h2>
  <p class="body-text" style="margin-top:4px">Carpet is one of the most used items in our household and yet is often the most ignored. Dirt, Sand, Food, Dander, Dead Skin, Hair, Grease and oil all build up over time. Sure you vacuum but is it doing enough? The answer is no! Let us take care of your carpet cleaning needs with our experienced technicans and the right equipment for the job.</p>
  <h2 class="small-head center" style="margin-top:7px;line-height:1.35">TILE &amp; GROUT CLEANING. THE RESULTS SPEAKS FOR THEMSELVES!!!</h2>
  <p class="body-text">It only takes once before you are a believer! Tile and grout build up layers of dirt and grime over time. mopping and scrubbing go a long way but from time to time they need a deep clean. That is where Bright Ridge Works comes in. Regardless of where the tile is we can make a difference for you!</p>
  <h2 class="small-head center" style="margin-top:7px">EMERGENCY WATER EXTRACTION!!!</h2>
  <p class="body-text">Water does serious damage. When there is an emergency, timingis of the essence. When that pipe breaks or a back up occurs call us and we'll be there. Our knowledgable staff and is equipped with the resources to give you the best chance of salvaging your carpet after a majorwater issue. Call Today to see how we can help!!!</p>
</section>
<div class="abs" style="left:593px;top:342px;width:180px;height:108px;background:var(--panel-grey)"></div>
<div class="photo" role="img" aria-label="Living room with sofa and carpet" style="left:600px;top:345px;width:83px;height:63px;background:linear-gradient(135deg,#c9a27e,#6e5a48)"></div>
<div class="photo" role="img" aria-label="Water running from a tap" style="left:688px;top:345px;width:80px;height:63px;background:linear-gradient(135deg,#e0e6ea,#8596a3)"></div>
<p class="abs center" style="left:600px;top:421px;width:166px;font-size:7.2px;font-weight:700;font-style:italic;line-height:1.25;color:var(--navy)">We are Available 24/7 for Emergency Water Extraction!!!</p>

<section class="panel dark" style="left:773px;width:180px">
  <h2 class="center" style="font-size:12.5px;font-weight:700;margin-top:12px">HANDYMAN SERVICES</h2>
  <p class="center" style="font-size:7.6px;font-weight:700;line-height:1.35;margin-top:9px">BRIGHT RIDGE WORKS HANDYMAN SERVICES, WHEN YOU JUST NEED TO GET IT DONE!!!</p>
</section>
<div class="photo" role="img" aria-label="Old wooden toolbox with hand tools" style="left:785px;top:170px;width:163px;height:140px;background:radial-gradient(ellipse at 55% 55%,#8a6a48 0%,#3d2e22 55%,#1a1512 100%)"></div>
<p class="body-text abs" style="left:782px;top:322px;width:164px;color:var(--white)">Bright Ridge Works is the answer to your home repair needs. Our staff of experienced technicians have the skills necessary to resolve all of your repair and maintenance issues. Minor Electrical, Plumbing, Heating and Air Conditioning. Honey Do Lists, Painting, Drywall Repair, Locks, Doors, Screens and Windows. Exterior Clean Up, Deck and Siding Repair. Appliance Repairs, Caulking, Tile...you name it we've got you covered</p>
<p class="abs center" style="left:773px;top:402px;width:180px;color:var(--white);font-size:10px;font-weight:700;font-style:italic">Call Us Today</p>
<p class="abs center" style="left:773px;top:416px;width:180px;color:var(--white);font-size:5.6px">to see how we can help you!!!</p>

<section class="panel light" style="left:953px;width:182px"></section>
<dl class="service-list">
  <div class="service-group"><dt>PLUMBING</dt><dd>Faucets<br>Sinks<br>Toilets<br>Garbage Disposals<br>Hot Water Tanks<br>Shut Off Valves<br>Leaks</dd></div>
  <div class="service-group"><dt>ELECTRICAL</dt><dd>Lighting<br>Outlets<br>Switches<br>GFCI<br>Ceiling Fans</dd></div>
  <div class="service-group"><dt>HVAC &amp; APPLIANCES</dt><dd>Air Conditioning<br>Furnaces<br>Hot Water Heaters<br>Fridges<br>Stoves<br>Dishwashers</dd></div>
  <div class="service-group"><dt>INTERIOR SERVICES</dt><dd>Painting<br>Drywall Repair<br>Screens/Windows<br>Locks<br>Tile Repair<br>Tile/Grout Cleaning<br>Caulking<br>Handrails</dd></div>
  <div class="service-group"><dt>EXTERIOR SERVICES</dt><dd>Gutter Cleaning<br>Power Washing<br>Deck Repairs<br>Staining/Sealing<br>Wood Rot Repairs<br>Minor Roof Repairs</dd></div>
</dl>
<div class="call-band">call today !!! &nbsp;(785) 555-0142</div>

</body>
</html>
```